Great Opportunity !! Masters in Business Analytics College Course

the size is Full Page, with bleed*
8”x 10.75" plus 0.25" bleed.
please leave one inch for footer
the purpose is attract students to join this college program .
this is for students in USA .
college age of around 24 years old
I am looking for a flyer that is unique and shows creativity .
A flyer that people would want to look at it because it is unique.
you can choose either vector, text ,or picture.
if you do picture it should be a white USA citizen wearing a white solid shirt and not long hair

Target Market(s)

USA students about 23 in age to join this college program

Industry/Entity Type

education

Colors
0054AA
0677BA
7BADD7
CADEEF
E8F1F8
0094D4
00A9DD
6FCCEA
C7EBF8
E9F6FB

Requirements
Must have
• the text should not be crowded .. .. .. the ad should not be full of text
Should not have
• not have very large text .. it should not be a flyer that is full of text .. you have to figure out how to avoid looking at the ad and it is very busy with text

```html
<!DOCTYPE html>
<html lang="en">
<head>
<meta charset="utf-8">
<title>Master's in Business Analytics – Open House Flyer</title>
<link href="https://fonts.googleapis.com/css2?family=Barlow+Condensed:wght@700;800&family=Poppins:wght@400;500;600;700;800&display=swap" rel="stylesheet">
<style>
  :root{
    --navy:#252a6e;
    --navy-deep:#1d2160;
    --blue:#1f5fc4;
    --yellow:#fcd20a;
    --white:#ffffff;
    --ink:#2b2f6e;
    --grey-text:#4a4d70;
    --backdrop:#7b7e88;
  }
  *{margin:0;padding:0;box-sizing:border-box}
  html,body{width:1200px;height:2392px;overflow:hidden;background:var(--backdrop)}
  .flyer{
    position:absolute;left:50px;top:468px;width:792px;height:1048px;
    transform:scale(1.3889);transform-origin:0 0;
    background:var(--white);overflow:hidden;
    font-family:'Poppins',sans-serif;color:var(--ink);
    box-shadow:0 2px 6px rgba(0,0,0,.25);
  }
  .bands{position:absolute;inset:0;width:792px;height:1048px}
  .display{font-family:'Barlow Condensed',sans-serif;font-weight:800;text-transform:uppercase}
  .abs{position:absolute;white-space:nowrap}
  .center{transform:translate(-50%,-50%)}
  .headline{left:396px;top:98px;transform:translate(-50%,-50%);font-weight:800;font-size:32px;line-height:41px;text-align:left;letter-spacing:-.2px}
  .headline .line-yellow{color:var(--yellow)}
  .headline .line-white{color:var(--white)}
  .headline-mark{left:690px;top:56px;font-weight:800;font-size:84px;line-height:84px;color:var(--white)}
  .tab-title{font-weight:600;font-size:22px;color:var(--white)}
  .tab-title .accent{color:var(--yellow)}
  .tab-hired{font-weight:700;font-size:22px;color:var(--yellow)}
  .check-row{display:flex;align-items:center;gap:22px;font-size:18.5px;color:var(--grey-text)}
  .check-row.hired{color:var(--ink);gap:30px}
  .check{display:inline-flex;align-items:center;gap:4px}
  .check svg{width:17px;height:17px}
  .event-date{left:438px;top:719px;font-size:16px;color:var(--ink)}
  .event-time{left:641px;top:715px;font-weight:600;font-size:16px;color:var(--white)}
  .event-email{left:410px;top:751px;font-size:16px;color:var(--ink)}
  .event-email b{font-weight:700}
  .accreditation{left:313px;top:825px;font-size:21px;line-height:27px;text-align:center;color:var(--ink)}
  .accreditation b{font-weight:700}
  .location{left:643px;top:800px;font-size:17.5px;line-height:23px;color:var(--white);text-align:center}
  .audience{left:160px;top:904px;font-size:19px;line-height:19px;color:var(--white);text-align:center}
  .format{left:530px;top:891px;font-size:13.5px;line-height:17px;color:var(--white)}
</style>
</head>
<body>
<main class="flyer">
  <svg class="bands" viewBox="0 0 792 1048">
    <defs>
      <radialGradient id="heroGlow" cx="0.42" cy="0.78" r="0.55">
        <stop offset="0" stop-color="#1f62cc"/>
        <stop offset="1" stop-color="#252a6e"/>
      </radialGradient>
      <linearGradient id="salaryBand" x1="0" y1="0" x2="1" y2="0">
        <stop offset="0.45" stop-color="#252a6e"/>
        <stop offset="1" stop-color="#1f62cc"/>
      </linearGradient>
      <linearGradient id="footBand" x1="0" y1="0" x2="1" y2="0">
        <stop offset="0" stop-color="#252a6e"/>
        <stop offset="0.45" stop-color="#1f5fc4"/>
        <stop offset="0.62" stop-color="#252a6e"/>
      </linearGradient>
      <linearGradient id="locationTag" x1="0" y1="0" x2="1" y2="0">
        <stop offset="0" stop-color="#111"/>
        <stop offset="1" stop-color="#bcbcbc"/>
      </linearGradient>
    </defs>
    <g aria-hidden="true">
      <polygon points="0,0 792,0 792,168 0,265" fill="url(#heroGlow)"/>
      <g stroke="#fff" fill="none">
        <polyline points="0,190 160,228 620,172" stroke-width="3"/>
        <polyline points="0,205 130,238 560,190" stroke-width="2"/>
        <polyline points="0,222 110,246" stroke-width="6"/>
      </g>
      <polygon points="0,232 170,240 0,250" fill="#fff"/>
      <polygon points="0,265 792,168 792,278 0,378" fill="var(--yellow)"/>
      <line x1="0" y1="262" x2="792" y2="164" stroke="#fff" stroke-width="4"/>
      <polygon points="0,378 792,278 792,405 0,513" fill="url(#salaryBand)"/>
      <line x1="0" y1="380" x2="792" y2="280" stroke="#fff" stroke-width="3"/>
      <polygon points="0,513 792,405 792,510 620,462 0,520" fill="var(--yellow)"/>
      <line x1="0" y1="515" x2="792" y2="408" stroke="#fff" stroke-width="3"/>
      <g stroke="var(--navy)" fill="none" stroke-width="1">
        <polyline points="380,506 610,460 792,512"/>
        <polyline points="420,509 615,468 792,518"/>
      </g>
      <polygon points="150,557 178,515 612,515 640,557" fill="var(--navy)"/>
      <g stroke="var(--navy)" stroke-width="1">
        <line x1="47" y1="557" x2="747" y2="557"/>
        <line x1="47" y1="593" x2="747" y2="593"/>
        <line x1="47" y1="634" x2="205" y2="634"/>
        <line x1="585" y1="634" x2="747" y2="634"/>
      </g>
      <polygon points="205,634 222,614 568,614 585,634 568,654 222,654" fill="none" stroke="var(--navy)" stroke-width="1.5"/>
      <polygon points="214,634 230,618 560,618 576,634 560,650 230,650" fill="var(--navy)"/>
      <polygon points="0,712 400,712 385,778 0,778" fill="var(--navy)"/>
      <polygon points="400,712 792,712 792,778 385,778" fill="var(--yellow)"/>
      <polygon points="390,778 405,712 410,712 395,778" fill="#fff"/>
      <polygon points="632,712 725,712 718,745 625,745" fill="var(--navy)"/>
      <line x1="410" y1="748" x2="745" y2="748" stroke="var(--navy)" stroke-width="1"/>
      <polygon points="597,797 792,797 792,853 587,853" fill="url(#locationTag)"/>
      <polygon points="597,797 640,797 630,853 587,853" fill="var(--yellow)"/>
      <path d="M613 812a9 9 0 0 1 9 9c0 7-9 16-9 16s-9-9-9-16a9 9 0 0 1 9-9z" fill="var(--navy)"/>
      <circle cx="613" cy="821" r="3.6" fill="var(--yellow)"/>
      <rect x="0" y="872" width="792" height="61" fill="url(#footBand)"/>
      <line x1="252" y1="887" x2="252" y2="922" stroke="#fff" stroke-width="1"/>
      <line x1="512" y1="887" x2="512" y2="922" stroke="#fff" stroke-width="1"/>
      <polygon points="281,868 322,868 316,928 275,928" fill="var(--yellow)"/>
    </g>

    <g class="display">
      <text class="program-title" transform="translate(394,289) rotate(-6.8) skewX(-12)" text-anchor="middle" font-size="47" fill="var(--navy)">
        <tspan x="0" y="-4">A Master's in Business Analytics-</tspan>
        <tspan x="8" y="34">Ridgeview State University ++</tspan>
      </text>
      <text class="program-sub" transform="translate(280,428) rotate(-6.8) skewX(-12)" text-anchor="middle" font-size="37" fill="var(--white)">
        <tspan x="0" y="-6">Can prepare you for in-demand</tspan>
        <tspan x="6" y="30">jobs with a median salary of</tspan>
      </text>
      <text class="salary" transform="translate(632,392) rotate(-6.8) skewX(-12)" text-anchor="middle" font-size="90" letter-spacing="4" fill="var(--yellow)"><tspan font-size="44" baseline-shift="26">$</tspan><tspan dx="6">100K</tspan><tspan font-size="56" fill="var(--white)" baseline-shift="22">+</tspan></text>
      <text class="open-house" transform="translate(224,765) skewX(-12)" text-anchor="middle" font-size="60" fill="var(--white)">Open House</text>
      <text class="duration-num" transform="translate(300,919) skewX(-12)" text-anchor="middle" font-size="48" fill="var(--navy)">21</text>
      <text class="duration-unit" transform="translate(346,919) skewX(-12)" text-anchor="start" font-size="48" fill="var(--white)">Months</text>
    </g>
  </svg>

  <div class="abs headline">
    <div class="line-yellow">DO YOU HAVE AN ANALYTICAL MIND</div>
    <div class="line-white">AND SEEKING A PROFITABLE CAREER</div>
  </div>
  <div class="abs headline-mark">?</div>

  <div class="abs center tab-title" style="left:395px;top:537px">National Career Data Review <span class="accent">2023</span></div>
  <div class="abs center check-row" style="left:397px;top:575px">
    <span class="check"><svg viewBox="0 0 20 20"><circle cx="10" cy="10" r="10" fill="var(--navy)"/><path d="M5.5 10.5l3 3 6-6.5" stroke="#fff" stroke-width="2.4" fill="none"/></svg>BI Developer</span>
    <span class="check"><svg viewBox="0 0 20 20"><circle cx="10" cy="10" r="10" fill="var(--navy)"/><path d="M5.5 10.5l3 3 6-6.5" stroke="#fff" stroke-width="2.4" fill="none"/></svg>Data Analyst</span>
    <span class="check"><svg viewBox="0 0 20 20"><circle cx="10" cy="10" r="10" fill="var(--navy)"/><path d="M5.5 10.5l3 3 6-6.5" stroke="#fff" stroke-width="2.4" fill="none"/></svg>Data Scientist</span>
    <span class="check"><svg viewBox="0 0 20 20"><circle cx="10" cy="10" r="10" fill="var(--navy)"/><path d="M5.5 10.5l3 3 6-6.5" stroke="#fff" stroke-width="2.4" fill="none"/></svg>Data Developer</span>
  </div>

  <div class="abs center tab-hired" style="left:395px;top:634px">Graduates were hired at:</div>
  <div class="abs center check-row hired" style="left:388px;top:681px">
    <span class="check"><svg viewBox="0 0 20 20"><circle cx="10" cy="10" r="10" fill="var(--navy)"/><path d="M5.5 10.5l3 3 6-6.5" stroke="#fff" stroke-width="2.4" fill="none"/></svg>Norvale</span>
    <span class="check"><svg viewBox="0 0 20 20"><circle cx="10" cy="10" r="10" fill="var(--navy)"/><path d="M5.5 10.5l3 3 6-6.5" stroke="#fff" stroke-width="2.4" fill="none"/></svg>Brightline</span>
    <span class="check"><svg viewBox="0 0 20 20"><circle cx="10" cy="10" r="10" fill="var(--navy)"/><path d="M5.5 10.5l3 3 6-6.5" stroke="#fff" stroke-width="2.4" fill="none"/></svg>Kestrel</span>
    <span class="check"><svg viewBox="0 0 20 20"><circle cx="10" cy="10" r="10" fill="var(--navy)"/><path d="M5.5 10.5l3 3 6-6.5" stroke="#fff" stroke-width="2.4" fill="none"/></svg>Voltara</span>
    <span class="check"><svg viewBox="0 0 20 20"><circle cx="10" cy="10" r="10" fill="var(--navy)"/><path d="M5.5 10.5l3 3 6-6.5" stroke="#fff" stroke-width="2.4" fill="none"/></svg>Summitcrest</span>
  </div>

  <div class="abs event-date">Wednesday, April <b>20<sup style="font-size:9px">th</sup></b></div>
  <div class="abs event-time">7:30 pm.</div>
  <div class="abs event-email"><b>Email</b> info@ridgeviewstate.edu &nbsp;for the link!</div>

  <div class="abs center accreditation">*** Elite Accreditation. A distinction held<br>by only <b>5%</b> of business schools globally.</div>
  <div class="abs location">Cedarbrook,<br>NJ, USA</div>

  <div class="abs center audience">Men &amp; Women<br>Program</div>
  <div class="abs format">Hybrid with one weekly<br>in-person evening meeting</div>
</main>
</body>
</html>
```